Flu 2019

Lockridge Regional Hospital is hosting a health fair/flu shot clinic this Fall. What she'd like to convey is the following:

Health Fair & Flu Clinic 2019
At the following locations from 10am - 1pm
Paint Rock - September 25 at Courthouse in Paint Rock
Eden - October 2 at Harlow Multipurpose Center
Menard - October 9 at Tasker Community Center
No cost flu shots available. Please bring insurance information.
Door prizes - Giveaways - Treats
Brought to you by Lockridge Regional Hospital

We would like to highlight the health fair which will be free to the community. We would like to also highlight the flu clinic; however, the no cost/bring insurance needs to be in smaller print.

```html
<!DOCTYPE html>
<html lang="en">
<head>
<meta charset="utf-8">
<title>Health Fair &amp; Flu Clinic 2019</title>
<link href="https://fonts.googleapis.com/css2?family=Montserrat:wght@500;600;800&family=Oswald:wght@700&family=Lato:wght@400;700&display=swap" rel="stylesheet">
<style>
  :root {
    --backdrop: #e9e6e1;
    --ink-dark: #151515;
    --ink-mid: #3b3b3b;
    --red: #cf4138;
    --red-deep: #a81f27;
    --white: #ffffff;
    --text-grey: #333333;
  }
  html, body { margin: 0; padding: 0; overflow: hidden; }
  body {
    width: 1200px; height: 1062px;
    background: var(--backdrop);
    position: relative;
    font-family: "Lato", sans-serif;
  }
  .flyer {
    position: absolute; left: 250px; top: 34px;
    width: 700px; height: 994px; overflow: hidden;
    background: radial-gradient(ellipse at 60% 45%, var(--ink-mid) 0%, #262626 45%, var(--ink-dark) 100%);
    box-shadow: 0 6px 24px rgba(0,0,0,.25);
  }
  .title-frame { position: absolute; left: 102px; top: 62px; width: 481px; height: 187px; }
  .title-small {
    position: absolute; top: 48px; left: 0; width: 700px; text-align: center;
    font-family: "Montserrat", sans-serif; font-weight: 600; font-size: 35px;
    letter-spacing: 2px; color: var(--white);
  }
  .title-main {
    position: absolute; top: 82px; left: 0; width: 700px; text-align: center;
    font-family: "Oswald", sans-serif; font-weight: 700; font-size: 92px; line-height: 1;
    color: var(--red); transform: scaleY(1.05); letter-spacing: 1px;
  }
  .title-year {
    position: absolute; top: 170px; left: 0; width: 700px; text-align: center;
    font-family: "Montserrat", sans-serif; font-weight: 800; font-size: 118px; line-height: 1;
    color: var(--white);
  }
  .portrait {
    position: absolute; left: 5px; top: 355px; width: 373px; height: 639px;
    background: linear-gradient(180deg, #4a4a4a 0%, #b9b9b9 45%, #eeeeee 70%, #f7f7f7 100%);
    border-radius: 160px 160px 0 0;
  }
  .stop { position: absolute; left: 0; width: 700px; height: 82px; }
  .stop-town {
    position: absolute; right: 335px; top: 28px;
    font-family: "Lato", sans-serif; font-size: 25px; color: var(--white); letter-spacing: .5px;
  }
  .stop-date {
    position: absolute; left: 378px; top: 0; width: 98px; height: 82px;
    background: var(--red); border-radius: 8px 0 0 8px; color: var(--white); text-align: center;
  }
  .stop-day { font-family: "Montserrat", sans-serif; font-weight: 800; font-size: 50px; line-height: 52px; display: block; }
  .stop-month { font-family: "Lato", sans-serif; font-size: 25px; line-height: 24px; display: block; }
  .stop-time {
    position: absolute; left: 481px; top: 0; width: 22px; height: 82px; background: #000;
    color: var(--white); font-size: 12px; font-weight: 700;
    writing-mode: vertical-rl; transform: rotate(180deg); text-align: center; line-height: 22px;
  }
  .stop-venue {
    position: absolute; left: 503px; top: 0; width: 197px; height: 82px; background: var(--white);
    box-sizing: border-box; padding: 10px 6px 0 10px;
    font-family: "Montserrat", sans-serif; font-weight: 500; font-size: 22px; line-height: 23px; color: var(--text-grey);
  }
  .perks { position: absolute; left: 445px; top: 634px; margin: 0; padding: 0; list-style: none; }
  .perk {
    display: flex; align-items: center; gap: 14px; height: 53px;
    font-family: "Lato", sans-serif; font-weight: 700; font-size: 27px; color: var(--white);
  }
  .perk svg { width: 36px; height: 36px; }
  .credits {
    position: absolute; left: 370px; top: 810px; width: 330px; height: 184px; background: var(--white);
    text-align: center;
  }
  .credits-lead { margin: 24px 0 0 0; font-size: 21px; color: var(--text-grey); padding-left: 30px; }
  .credits-name {
    margin: 14px 0 0 30px; font-family: "Lato", sans-serif; font-weight: 700; font-size: 22px; color: #111;
    display: flex; align-items: center; justify-content: center; gap: 8px;
  }
  .credits-name::before { content: ""; width: 14px; height: 14px; background: #111; border-radius: 50%; }
  .credits-web { margin: 34px 0 0 30px; font-size: 11px; font-weight: 700; color: #111; }
  .badge { position: absolute; left: 242px; top: 704px; width: 178px; height: 178px; }
  .badge-text {
    position: absolute; left: 242px; top: 736px; width: 178px; text-align: center; color: var(--white);
  }
  .badge-free { font-family: "Montserrat", sans-serif; font-weight: 800; font-size: 40px; line-height: 42px; display: block; }
  .badge-sub { font-family: "Lato", sans-serif; font-weight: 700; font-size: 16px; line-height: 19px; display: block; }
  .badge-note { font-size: 7px; display: block; margin-top: 10px; border-top: 1px solid #fff; width: 66px; margin-left: 56px; padding-top: 3px; }
</style>
</head>
<body>
  <main class="flyer">
    <svg class="title-frame" viewBox="0 0 481 187">
      <polyline points="80,3 3,3 3,184 80,184" fill="none" stroke="#cf4138" stroke-width="3"/>
      <polyline points="401,3 478,3 478,184 401,184" fill="none" stroke="#cf4138" stroke-width="3"/>
    </svg>
    <div class="title-small">HEALTH FAIR &amp;</div>
    <div class="title-main">FLU CLINIC</div>
    <div class="title-year">2019</div>

    <div class="portrait" role="img" aria-label="Photo of a smiling doctor in a white coat with a stethoscope, arms crossed"></div>

    <section class="stop" style="top:312px">
      <span class="stop-town">PAINT ROCK</span>
      <div class="stop-date"><span class="stop-day">25</span><span class="stop-month">Sep</span></div>
      <div class="stop-time">10am -1pm</div>
      <div class="stop-venue">Courthouse in<br>Paint Rock</div>
    </section>
    <section class="stop" style="top:416px">
      <span class="stop-town">EDEN</span>
      <div class="stop-date"><span class="stop-day">02</span><span class="stop-month">Oct</span></div>
      <div class="stop-time">10am -1pm</div>
      <div class="stop-venue">Harlow<br>Multipurpose<br>Center</div>
    </section>
    <section class="stop" style="top:522px">
      <span class="stop-town">MENARD</span>
      <div class="stop-date"><span class="stop-day">09</span><span class="stop-month">Oct</span></div>
      <div class="stop-time">10am -1pm</div>
      <div class="stop-venue">Tasker<br>Community<br>Center</div>
    </section>

    <ul class="perks">
      <li class="perk">
        <svg viewBox="0 0 36 36"><circle cx="18" cy="18" r="16" fill="none" stroke="#cf4138" stroke-width="2"/><rect x="11" y="11" width="10" height="14" fill="#cf4138"/><path d="M21 18h6M24 15l3 3-3 3" stroke="#cf4138" stroke-width="2" fill="none"/></svg>
        Door prizes
      </li>
      <li class="perk">
        <svg viewBox="0 0 36 36"><circle cx="18" cy="18" r="16" fill="none" stroke="#cf4138" stroke-width="2"/><path d="M10 12h16l-8 13z" fill="none" stroke="#cf4138" stroke-width="2.5"/></svg>
        Giveaways
      </li>
      <li class="perk">
        <svg viewBox="0 0 36 36"><circle cx="18" cy="18" r="16" fill="#cf4138" fill-opacity=".35" stroke="#cf4138" stroke-width="2"/><path d="M11 14h14l-2 12h-10z" fill="#cf4138"/><circle cx="18" cy="12" r="4" fill="#cf4138"/></svg>
        Treats
      </li>
    </ul>

    <section class="credits">
      <p class="credits-lead">Brought to you</p>
      <p class="credits-name">Lockridge Regional Hospital</p>
      <p class="credits-web">www.lockridgeregional.hospital</p>
    </section>

    <svg class="badge" viewBox="0 0 178 178">
      <circle cx="89" cy="89" r="88" fill="#c3262f"/>
      <circle cx="89" cy="89" r="72" fill="#b21f29" stroke="#ffffff" stroke-width="1.5"/>
    </svg>
    <div class="badge-text">
      <span class="badge-free">FREE</span>
      <span class="badge-sub">TO THE<br>COMMUNITY</span>
      <span class="badge-note">No cost / bring insurance</span>
    </div>
  </main>
</body>
</html>
```